Business Card Project

Hello,

Please find attached files for use for our business card design.

We have attached all the version of the trade licensing council to the project for insertion onto our business card.

Details to be on the card are:
We are a construction management company. Please ensure that there is space to add our personal contact details. We would like the cards to be double sided with our logo on one side and our details on the other

Thanks,

Marcus

Good Evening,

Please ensure with all design submissions, that the 'certified works overseer' logo is on the card designs.

Thanks,

Marcus

Industry/Entity Type

Construction

```html
<!DOCTYPE html>
<html lang="en">
<head>
<meta charset="utf-8">
<title>Norland Group – Business Card</title>
<link rel="stylesheet" href="https://fonts.googleapis.com/css2?family=Marcellus+SC&family=Raleway:wght@300;400;600&display=swap">
<style>
  :root {
    --page-bg: #e6e6e8;
    --brand-brown: #43200f;
    --card-white: #ffffff;
    --slate: #5f6062;
    --contact-grey: #b4b5b7;
    --navy: #1c3a6e;
    --line-light: #e9e2dc;
    --shadow: rgba(0, 0, 0, 0.28);
  }
  * { box-sizing: border-box; margin: 0; padding: 0; }
  html, body {
    width: 1200px;
    height: 900px;
    overflow: hidden;
    background: var(--page-bg);
  }
  .sheet {
    width: 1200px;
    height: 900px;
    display: flex;
    align-items: center;
    justify-content: center;
    gap: 50px;
  }
  .card {
    position: relative;
    width: 540px;
    height: 310px;
    overflow: hidden;
    box-shadow: 4px 6px 12px var(--shadow);
  }

  /* Front: brand side */
  .card--front {
    background: var(--brand-brown);
    display: flex;
    align-items: center;
    justify-content: center;
  }
  .brand-lockup {
    display: flex;
    align-items: center;
    gap: 22px;
    width: 100%;
    padding: 0 24px;
  }
  .brand-rule {
    flex: 1;
    height: 9px;
    border-top: 2px solid var(--line-light);
    border-bottom: 2px solid var(--line-light);
  }
  .brand-mark {
    display: flex;
    align-items: center;
    gap: 12px;
  }
  .brand-square {
    width: 22px;
    height: 22px;
    background: var(--card-white);
  }
  .brand-name {
    font-family: "Marcellus SC", serif;
    font-size: 44px;
    color: var(--card-white);
    letter-spacing: 1px;
    white-space: nowrap;
  }

  /* Back: contact side */
  .card--back { background: var(--slate); }
  .card__split {
    position: absolute;
    inset: 0;
    width: 100%;
    height: 100%;
  }
  .credential {
    position: absolute;
    top: 18px;
    left: 18px;
    display: flex;
    align-items: center;
    gap: 8px;
  }
  .credential__badge {
    width: 30px;
    height: 30px;
    border-radius: 50%;
    border: 2px solid var(--navy);
    background: #eef0f4;
  }
  .credential__name {
    font-family: "Raleway", sans-serif;
    font-weight: 600;
    font-size: 12px;
    color: var(--navy);
  }
  .contact {
    position: absolute;
    right: 28px;
    top: 120px;
    text-align: right;
    font-family: "Raleway", sans-serif;
    font-weight: 300;
    color: var(--contact-grey);
  }
  .contact__name {
    font-family: "Marcellus SC", serif;
    font-weight: 400;
    font-size: 32px;
    color: var(--card-white);
    margin-bottom: 8px;
  }
  .contact__phone { font-size: 20px; margin-bottom: 10px; }
  .contact__line { font-size: 15px; line-height: 1.35; }
  .contact__address { font-size: 12px; line-height: 1.45; margin-top: 4px; }
</style>
</head>
<body>
  <main class="sheet">
    <section class="card card--front" aria-label="Card front">
      <div class="brand-lockup">
        <span class="brand-rule"></span>
        <div class="brand-mark">
          <span class="brand-square"></span>
          <span class="brand-name">Norland Group</span>
        </div>
        <span class="brand-rule"></span>
      </div>
    </section>

    <section class="card card--back" aria-label="Card back">
      <svg class="card__split" viewBox="0 0 540 310" preserveAspectRatio="none" aria-hidden="true">
        <polygon points="0,0 275,0 0,298" fill="#ffffff"/>
      </svg>
      <div class="credential">
        <span class="credential__badge"></span>
        <span class="credential__name">Certified Works Overseer</span>
      </div>
      <div class="contact">
        <p class="contact__name">Name Surname</p>
        <p class="contact__phone">(000)0 000-0000</p>
        <p class="contact__line">email@website.com</p>
        <p class="contact__line">www.website.com</p>
        <p class="contact__address">Street, Building, Zip Code<br>City, Country</p>
      </div>
    </section>
  </main>
</body>
</html>
```